Label Design for RTD Cocktail Line Tovelin Spirits

Tovelin Spirits is a line of Indian-inspired artisan cocktails that "brings the bartender home" for professional men and women who like the finer things in life but don’t always have the time to treat themselves. No need for a multitude of expensive and hard-to-find ingredients, time consuming recipes, or a mixologist.

Our line of 3 open and serve cocktails blends a range of premium spirits with exotic ingredients so you can conveniently raise a glass for any of life’s celebrations.

Our bottle is the 750ml Claret bottle with Quarnet (screw cap) closure and will be covered entirely in a shrink sleeve (so potentially anything can be designed for any part of the bottle). We want the bottle to pop on the shelf so it should look different than what’s already out there (Velvet Moth, Galdrova, Merlusa ready to drink cocktails). We are looking for a sexy design that's polished/sleek.
Updates

Project Deadline Extended
Reason: Hello designers! Tovelin Spirits is so impressed with what we have received thus far and we would like to give some of the designers a few extra days to make the edits we requested. It's never too late to submit! Thank you all!

Industry/Entity Type

It Professional

Requirements
Must have
• Front of bottle
* “Tovelin Spirits” name and Peacock Logo- but feel free to pull the elements apart and use them on the bottle in different ways
* Open & Serve
* 12% ALC/VOL
* 750 ml
* 3 different labels in a theme for
-Borvelle
-Faluntera
-Pomadrine

Borvelle Ideas- soft brown palate, the ingredients in chai spice (cloves, cardamom pods, nutmeg, black peppercorns, star anise, and cinnamon stick)

Faluntera Ideas -cool and refreshing, pale green shade (not clashing with logo), graphics of fresh mint leaves, green chili, lime, cucumber

Pomadrine Ideas- soft/pale pink shades, graphics of lychi fruit (outer red shell and inner pink flesh), ginger

Back of bottle
* explanation of the 3 cocktails
Borvelle: Forget what you think you know about chai, this is not the Queen’s tea-time drink! Borvelle is a smooth, sweetly -spiced cocktail made with vodka, black tea, and a combination of aromatic spices. This velvety cocktail is rich without being heavy. Enjoy chilled or over ice anytime.

Faluntera: Faluntera can’t make up its mind! This fusion of zesty lime, sweet mint, earthy cucumber and spicy chilies is so refreshing you’ll crave it on a hot summer day or a cool winter’s night. The exotic botanicals in gin add a complexity to the cocktail making this a refreshing but potent drink! Enjoy chilled or over ice anytime.

Pomadrine: East meet West. Delicate lychi meet hard-hitting whiskey. Pomadrine will tempt you senses with flavor, fragrance and beauty. The peppery kick of ginger and the intensity of the un-aged whiskey are softened by lychi’s intoxicating scent and subtle, sweet finish.

Please include
1. Bottled By QRW Spirits Company
2. Sample barcode (where you would place it in your design)
3. www.TovelinSpirits.example
4. GOVERNMENT WARNING: (1) According to the Surgeon General, women should not drink alcoholic beverages during pregnancy because of the risk of birth defects. (2) Consumption of alcoholic beverages impairs your ability to drive a car or operate machinery, and may cause health problems.

Optional to include
*"Bring the Bartender Home"
*"Tovelin Spirits” name and Peacock Logo on the back
*Entirely black sleeve with contrasting design

FYI the Fonts used in our logo are Geosans Light and Prakrta, but feel free to use other complimentary fonts on the other aspects.
Nice to have
• Optional to include

```html
<!DOCTYPE html>
<html lang="en">
<head>
<meta charset="utf-8">
<title>Tovelin Spirits – Cocktail Sleeve Labels</title>
<link rel="stylesheet" href="https://fonts.googleapis.com/css2?family=Josefin+Sans:wght@100;300;400&display=swap">
<style>
  :root {
    --page: #ffffff;
    --sleeve: #3a3a3c;
    --ink: #2f2f31;
    --mint: #2fb56c;
    --chai: #c8c4b5;
    --lychee: #f1a7a9;
  }
  html, body {
    margin: 0;
    padding: 0;
    width: 1200px;
    height: 900px;
    overflow: hidden;
    background: var(--page);
  }
  .label-range {
    display: block;
    width: 1200px;
    height: 900px;
    font-family: "Josefin Sans", sans-serif;
  }
  .sleeve-body { fill: var(--sleeve); }
  .brand-name { font-family: "Josefin Sans", sans-serif; font-weight: 400; letter-spacing: 0.5px; }
  .brand-sub { font-family: "Josefin Sans", sans-serif; font-weight: 300; letter-spacing: 2.5px; }
  .flavour-name { font-family: "Josefin Sans", sans-serif; font-weight: 100; fill: var(--ink); }
  .spec-line { font-family: "Josefin Sans", sans-serif; font-weight: 300; font-size: 8.5px; }
  .back-copy { font-family: "Josefin Sans", sans-serif; font-weight: 300; font-size: 4.6px; fill: var(--mint); }
  .mint { fill: var(--mint); }
  .chai { fill: var(--chai); }
  .lychee { fill: var(--lychee); }
  .ink { fill: var(--ink); }
</style>
</head>
<body>
<svg class="label-range" viewBox="0 0 1200 900" xmlns="http://www.w3.org/2000/svg">
  <defs>
    <path id="sleeve-shape" d="M-30,200 C-30,245 -80,255 -80,300 V755 Q-80,770 -65,770 H65 Q80,770 80,755 V300 C80,255 30,245 30,200 Z"/>
    <path id="splash-shape" d="M-62,410 C-40,398 -20,406 0,398 C20,392 40,404 56,400 C72,396 76,418 70,440 C66,462 78,486 72,512 C66,540 74,566 66,594 C58,624 68,652 58,680 C50,704 36,720 20,726 C4,732 -20,724 -36,730 C-52,736 -64,726 -68,710 C-72,690 -66,660 -70,630 C-74,600 -66,570 -70,540 C-74,510 -66,480 -70,450 C-72,430 -72,416 -62,410 Z"/>
  </defs>

  <!-- Faluntera front -->
  <g class="bottle bottle--faluntera" transform="translate(185 0)">
    <rect class="neck-band mint" x="-30" y="100" width="60" height="104"/>
    <rect class="cap-lip mint" x="-31" y="78" width="62" height="34" rx="5"/>
    <circle class="ink" cx="0" cy="152" r="4"/>
    <text class="brand-name ink" x="0" y="177" text-anchor="middle" font-size="11">Tovelin</text>
    <text class="brand-sub ink" x="0" y="187" text-anchor="middle" font-size="4">SPIRITS</text>
    <use href="#sleeve-shape" class="sleeve-body"/>
    <circle class="mint" cx="0" cy="322" r="8"/>
    <text class="brand-name mint" x="0" y="370" text-anchor="middle" font-size="22">Tovelin</text>
    <text class="brand-sub mint" x="0" y="383" text-anchor="middle" font-size="5">SPIRITS</text>
    <use href="#splash-shape" class="mint" role="img" aria-label="Paint splash texture in fresh mint green"/>
    <text class="flavour-name" transform="translate(-8 712) rotate(-90)" font-size="60" textLength="305" lengthAdjust="spacingAndGlyphs">FALUNTERA</text>
    <text class="spec-line mint" x="0" y="746" text-anchor="middle" textLength="146" lengthAdjust="spacingAndGlyphs">12% ALC/VOL | OPEN &amp; SERVE | 750 ml</text>
  </g>

  <!-- Back sleeve -->
  <g class="bottle bottle--back" transform="translate(468 0)">
    <rect class="neck-band mint" x="-30" y="100" width="60" height="104"/>
    <rect class="cap-lip mint" x="-31" y="78" width="62" height="34" rx="5"/>
    <circle class="ink" cx="0" cy="152" r="4"/>
    <text class="brand-name ink" x="0" y="177" text-anchor="middle" font-size="11">Tovelin</text>
    <text class="brand-sub ink" x="0" y="187" text-anchor="middle" font-size="4">SPIRITS</text>
    <use href="#sleeve-shape" class="sleeve-body"/>
    <circle class="mint" cx="0" cy="405" r="7"/>
    <text class="brand-name mint" x="0" y="446" text-anchor="middle" font-size="17">Tovelin</text>
    <text class="brand-sub mint" x="0" y="456" text-anchor="middle" font-size="4">SPIRITS</text>
    <text class="back-copy" text-anchor="middle">
      <tspan x="0" y="470">Faluntera can't make up its mind! This fusion of zesty</tspan>
      <tspan x="0" y="477">lime, sweet mint, earthy cucumber and spicy chilies is</tspan>
      <tspan x="0" y="484">so refreshing you'll crave it on a hot summer day or a</tspan>
      <tspan x="0" y="491">cool winter's night. The exotic botanicals in gin add a</tspan>
      <tspan x="0" y="498">complexity to the cocktail making this a refreshing but</tspan>
      <tspan x="0" y="505">potent drink! Enjoy chilled or over ice anytime.</tspan>
      <tspan x="0" y="521">Bottled By QRW Spirits Company</tspan>
      <tspan x="0" y="531">www.TovelinSpirits.example</tspan>
      <tspan x="0" y="549">GOVERNMENT WARNING:</tspan>
      <tspan x="0" y="556">(1) According to the Surgeon General, women should</tspan>
      <tspan x="0" y="563">not drink alcoholic beverages during pregnancy because</tspan>
      <tspan x="0" y="570">of the risk of birth defects.</tspan>
      <tspan x="0" y="577">(2) Consumption of alcoholic beverages impairs your ability</tspan>
      <tspan x="0" y="584">to drive a car or operate machinery, and may cause</tspan>
      <tspan x="0" y="591">health problems.</tspan>
    </text>
  </g>

  <!-- Borvelle front -->
  <g class="bottle bottle--borvelle" transform="translate(745 0)">
    <rect class="neck-band chai" x="-30" y="100" width="60" height="104"/>
    <rect class="cap-lip chai" x="-31" y="78" width="62" height="34" rx="5"/>
    <circle class="ink" cx="0" cy="152" r="4"/>
    <text class="brand-name ink" x="0" y="177" text-anchor="middle" font-size="11">Tovelin</text>
    <text class="brand-sub ink" x="0" y="187" text-anchor="middle" font-size="4">SPIRITS</text>
    <use href="#sleeve-shape" class="sleeve-body"/>
    <circle class="chai" cx="0" cy="322" r="8"/>
    <text class="brand-name chai" x="0" y="370" text-anchor="middle" font-size="22">Tovelin</text>
    <text class="brand-sub chai" x="0" y="383" text-anchor="middle" font-size="5">SPIRITS</text>
    <use href="#splash-shape" class="chai" role="img" aria-label="Paint splash texture in soft chai beige"/>
    <text class="flavour-name" transform="translate(-8 712) rotate(-90)" font-size="60" textLength="290" lengthAdjust="spacingAndGlyphs">BORVELLE</text>
    <text class="spec-line chai" x="0" y="746" text-anchor="middle" textLength="146" lengthAdjust="spacingAndGlyphs">12% ALC/VOL | OPEN &amp; SERVE | 750 ml</text>
  </g>

  <!-- Pomadrine front -->
  <g class="bottle bottle--pomadrine" transform="translate(1020 0)">
    <rect class="neck-band lychee" x="-30" y="100" width="60" height="104"/>
    <rect class="cap-lip lychee" x="-31" y="78" width="62" height="34" rx="5"/>
    <circle class="ink" cx="0" cy="152" r="4"/>
    <text class="brand-name ink" x="0" y="177" text-anchor="middle" font-size="11">Tovelin</text>
    <text class="brand-sub ink" x="0" y="187" text-anchor="middle" font-size="4">SPIRITS</text>
    <use href="#sleeve-shape" class="sleeve-body"/>
    <circle class="lychee" cx="0" cy="322" r="8"/>
    <text class="brand-name lychee" x="0" y="370" text-anchor="middle" font-size="22">Tovelin</text>
    <text class="brand-sub lychee" x="0" y="383" text-anchor="middle" font-size="5">SPIRITS</text>
    <use href="#splash-shape" class="lychee" role="img" aria-label="Paint splash texture in pale lychee pink"/>
    <text class="flavour-name" transform="translate(-8 712) rotate(-90)" font-size="60" textLength="305" lengthAdjust="spacingAndGlyphs">POMADRINE</text>
    <text class="spec-line lychee" x="0" y="746" text-anchor="middle" textLength="146" lengthAdjust="spacingAndGlyphs">12% ALC/VOL | OPEN &amp; SERVE | 750 ml</text>
  </g>
</svg>
</body>
</html>
```